TCH Business cards

We are a medium sized property company based in London and require a logo, Business card which reflects a professional company and incorporates our catchy name.

Our statement is (Building for the future) we like colours such as royal blue, greens and light browns but will look at anything.

Contact Information for Business Card

Tidecrest Holdings Limited
Unit 4, 3-5 Parbrook Lane
London
SE21 7QX

Web: www.tidecrestholdings.example

Email: tidecrestltd@mailbox.example

Telephone: +44-208-555-0142
Fax: +44-208-555-0187

```html
<!DOCTYPE html>
<html lang="en">
<head>
<meta charset="utf-8">
<title>TCH Business Card</title>
<link rel="stylesheet" href="https://fonts.googleapis.com/css2?family=Lato:wght@400;700;900&display=swap">
<style>
  :root {
    --backdrop: #2b2b2b;
    --card: #f7f7f7;
    --navy: #0f2366;
    --name-navy: #1c1a63;
    --ink: #2a2a2a;
    --contact-grey: #7d7d7d;
    --band-grey: #4a4a4a;
    --icon-white: #ffffff;
  }
  * { margin: 0; padding: 0; box-sizing: border-box; }
  html, body {
    width: 1200px;
    height: 873px;
    overflow: hidden;
    background: var(--backdrop);
    font-family: "Lato", Arial, sans-serif;
  }
  .business-card {
    position: absolute;
    left: 100px;
    top: 150px;
    width: 1000px;
    height: 572px;
    background: linear-gradient(135deg, #ffffff 0%, var(--card) 60%, #ececec 100%);
    overflow: hidden;
    box-shadow: 0 20px 50px rgba(0,0,0,0.5);
  }
  .holder {
    position: absolute;
    left: 90px;
    top: 120px;
  }
  .holder-name {
    font-weight: 900;
    font-size: 34px;
    color: var(--name-navy);
    letter-spacing: 0.3px;
  }
  .holder-role {
    font-size: 21px;
    color: var(--ink);
    margin-top: 2px;
  }
  .brand {
    position: absolute;
    left: 560px;
    top: 170px;
    width: 360px;
    display: flex;
    align-items: center;
    gap: 16px;
  }
  .brand-square {
    width: 46px;
    height: 46px;
    background: var(--band-grey);
    flex: none;
  }
  .brand-name {
    font-weight: 400;
    font-size: 27px;
    line-height: 1.15;
    color: var(--band-grey);
  }
  .icon-tab {
    position: absolute;
    left: 0;
    top: 290px;
    width: 82px;
    height: 240px;
    background: var(--navy);
    border-radius: 0 14px 14px 0;
    display: flex;
    flex-direction: column;
    justify-content: space-around;
    align-items: center;
    padding: 14px 0;
  }
  .icon-tab svg { width: 30px; height: 30px; }
  .contact-list {
    position: absolute;
    left: 120px;
    top: 298px;
    list-style: none;
  }
  .contact-list li {
    font-size: 21px;
    color: var(--contact-grey);
    height: 45px;
    line-height: 45px;
    letter-spacing: 0.4px;
  }
  .card-bands {
    position: absolute;
    left: 0;
    bottom: 0;
    width: 1000px;
    height: 110px;
  }
</style>
</head>
<body>
  <main class="business-card">
    <div class="holder">
      <h1 class="holder-name">Daniel Harrow</h1>
      <p class="holder-role">Owner / Founder</p>
    </div>

    <div class="brand">
      <div class="brand-square"></div>
      <p class="brand-name">Tidecrest Holdings Limited</p>
    </div>

    <div class="icon-tab">
      <svg viewBox="0 0 24 24" aria-label="Mobile"><rect x="6" y="2" width="12" height="20" rx="2" fill="none" stroke="#fff" stroke-width="2"/><circle cx="12" cy="18.5" r="1" fill="#fff"/></svg>
      <svg viewBox="0 0 24 24" aria-label="Fax"><rect x="7" y="3" width="10" height="5" fill="#fff"/><rect x="3" y="9" width="18" height="8" rx="1.5" fill="#fff"/><rect x="7" y="14" width="10" height="7" fill="#fff" stroke="#0f2366" stroke-width="1.5"/></svg>
      <svg viewBox="0 0 24 24" aria-label="Email"><rect x="2" y="5" width="20" height="14" fill="none" stroke="#fff" stroke-width="2"/><path d="M2 5l10 8 10-8" fill="none" stroke="#fff" stroke-width="2"/></svg>
      <svg viewBox="0 0 24 24" aria-label="Website"><path d="M10 14l4-4" stroke="#fff" stroke-width="2"/><path d="M11 7l2-2a4 4 0 0 1 6 6l-2 2M13 17l-2 2a4 4 0 0 1-6-6l2-2" fill="none" stroke="#fff" stroke-width="2" stroke-linecap="round"/></svg>
      <svg viewBox="0 0 24 24" aria-label="Address"><path d="M12 2a7 7 0 0 0-7 7c0 5 7 13 7 13s7-8 7-13a7 7 0 0 0-7-7z" fill="#fff"/><circle cx="12" cy="9" r="2.6" fill="#0f2366"/></svg>
    </div>

    <ul class="contact-list">
      <li>+44-208-555-0142</li>
      <li>+44-208-555-0187</li>
      <li>tidecrestltd@mailbox.example</li>
      <li>www.tidecrestholdings.example</li>
      <li>Unit 4, 3-5 Parbrook Lane London SE21 7QX</li>
    </ul>

    <svg class="card-bands" viewBox="0 0 1000 110" preserveAspectRatio="none">
      <path d="M0 110 L0 82 L520 70 Q548 69 560 58 L560 110 Z" fill="var(--band-grey)"/>
      <path d="M560 110 L560 58 Q574 38 610 36 L1000 20 L1000 110 Z" fill="#ffffff"/>
      <path d="M575 110 Q582 50 625 48 L1000 34 L1000 110 Z" fill="var(--navy)"/>
      <path d="M560 110 L560 72 Q566 100 575 110 Z" fill="var(--band-grey)"/>
    </svg>
  </main>
</body>
</html>
```